Seafood restaurant menu

I am looking for a new menu design for my cajun seafood restaurant. I want something modern and simple. Our menu is very small so just one page front and back. Preferred, menu size is (4.25"x11"), I have attach some images, but we will have more to give.
Updates

Need to give designer more time

Target Market(s)

young to middle aged customers

Industry/Entity Type

Restaurant Food industry

Colors
EB3D1F
EC4F4E
F09395
F8D3D4
FCEDEE

Requirements
Must have
• creativity and interesting
Nice to have
• I would like to see a clean and simple menu, but with good color placement and photos of the dishes

```html
<!DOCTYPE html>
<html lang="en">
<head>
<meta charset="utf-8">
<title>Reddie's Boil Shack Menu</title>
<link href="https://fonts.googleapis.com/css2?family=Arimo:wght@400;700&family=Kaushan+Script&display=swap" rel="stylesheet">
<style>
:root{
  --blush:#f8d3d4;
  --pink-text:#f6c9cb;
  --charcoal:#2b2b2b;
  --ink:#1a1a1a;
  --white:#ffffff;
  --red:#e0252b;
  --orange:#f05a22;
  --chili:#4caf3c;
}
*{margin:0;padding:0;box-sizing:border-box}
html,body{width:1200px;height:3107px;overflow:hidden;background:var(--blush)}
.menu{position:relative;width:1200px;height:3107px;background:var(--blush);font-family:'Arimo',Arial,sans-serif;color:var(--white);font-variant:small-caps}
.backdrop{position:absolute;left:0;top:0;width:1200px;height:3107px}
.hero{position:absolute;left:0;top:0;width:1200px;height:560px}
.abs{position:absolute;white-space:nowrap;transform:translateY(-50%)}
.section-title{font-family:'Kaushan Script',cursive;font-variant:normal;color:var(--pink-text);font-size:86px;line-height:1}
.code{left:142px;font-size:37px;font-variant:normal;color:#f3c3c5}
.item{left:253px;font-size:37px;letter-spacing:1px}
.price{right:169px;font-size:37px;text-align:right}
.price.seasonal{font-size:31px}
.note{left:248px;font-size:26px}
.detail{left:253px;font-size:22px;letter-spacing:.5px}
.item small{font-size:27px}
.divider{position:absolute;left:141px;height:30px}
.divider .squares{position:absolute;left:0;top:0;width:30px;height:30px}
.divider .rule{position:absolute;left:56px;top:13px;height:4px;background:var(--red)}
.choice{font-size:38px;letter-spacing:1px;text-align:center}
.col-rule{position:absolute;left:629px;top:2328px;width:4px;height:289px;background:var(--red)}
.chili{display:inline-block;vertical-align:-4px;margin-right:4px}
.drink{left:0;width:1200px;text-align:center;font-size:40px}
.drink-sub{left:0;width:1200px;text-align:center;font-size:20px;letter-spacing:1px}
.footer-title{left:0;width:1200px;text-align:center;color:var(--ink);font-weight:700;font-size:39px;letter-spacing:1px}
.footer-address{left:0;width:1200px;text-align:center;color:var(--ink);font-weight:700;font-size:20px}
.brand{color:var(--red);font-family:'Arimo',Arial,sans-serif;font-weight:700;font-size:17px;text-align:center;line-height:1.1;width:110px}
.brand .dot{display:block;width:34px;height:34px;border-radius:50%;background:var(--red);margin:0 auto 6px}
</style>
</head>
<body>
<main class="menu">
  <svg class="backdrop" viewBox="0 0 1200 3107" aria-hidden="true">
    <polygon points="0,506 600,380 1200,506 1200,2964 0,2964" fill="#2b2b2b"/>
  </svg>

  <svg class="hero" viewBox="0 0 1200 560">
    <defs>
      <radialGradient id="boilTones" cx="50%" cy="50%" r="60%">
        <stop offset="0" stop-color="#d8553a"/>
        <stop offset=".6" stop-color="#b32a1c"/>
        <stop offset="1" stop-color="#5a1a12"/>
      </radialGradient>
    </defs>
    <ellipse cx="600" cy="300" rx="462" ry="248" fill="url(#boilTones)" role="img" aria-label="Photo of a seafood boil with lobster tail, shrimp and snow crab legs in garlic butter sauce"/>
    <ellipse cx="570" cy="297" rx="505" ry="240" fill="none" stroke="var(--orange)" stroke-width="6"/>
    <ellipse cx="630" cy="297" rx="505" ry="240" fill="none" stroke="#c8202a" stroke-width="6"/>
  </svg>

  <h2 class="abs section-title" style="left:247px;top:638px">Seafood By the lb</h2>
  <span class="abs code" style="top:732px">L1</span><span class="abs item" style="top:732px">Crawfish</span><span class="abs price" style="top:732px">18</span>
  <span class="abs code" style="top:790px">L2</span><span class="abs item" style="top:790px">Shrimp w/ head</span><span class="abs price" style="top:790px">18</span>
  <span class="abs code" style="top:849px">L3</span><span class="abs item" style="top:849px">Shrimp w/o head deveined</span><span class="abs price" style="top:849px">20</span>
  <span class="abs code" style="top:907px">L4</span><span class="abs item" style="top:907px">Clams</span><span class="abs price" style="top:907px">18</span>
  <span class="abs code" style="top:965px">L5</span><span class="abs item" style="top:965px">Mussels</span><span class="abs price" style="top:965px">18</span>
  <span class="abs code" style="top:1023px">L6</span><span class="abs item" style="top:1023px">Snow Crab Legs</span><span class="abs price" style="top:1023px">39</span>
  <span class="abs code" style="top:1082px">L7</span><span class="abs item" style="top:1082px">Lobster Tail</span><span class="abs price seasonal" style="top:1082px">seasonal</span>
  <span class="abs code" style="top:1140px">L8</span><span class="abs item" style="top:1140px">King Crab Legs</span><span class="abs price seasonal" style="top:1140px">seasonal</span>

  <div class="divider" style="top:1199px"><svg class="squares" viewBox="0 0 30 30"><rect width="13" height="13" fill="#e0252b"/><rect x="17" width="13" height="13" fill="#e0252b"/><rect y="17" width="13" height="13" fill="#e0252b"/><rect x="17" y="17" width="13" height="13" fill="#e0252b"/></svg><div class="rule" style="width:165px"></div></div>

  <h2 class="abs section-title" style="left:247px;top:1315px">Seafood Plates</h2>
  <p class="abs note" style="top:1400px">(all plates come with 1 flavor, 1 corn, sausages &amp; 1 potato)</p>
  <span class="abs code" style="top:1464px">P1</span><span class="abs item" style="top:1464px">Seafood Plate 2lb <small>(1 flavor)</small></span><span class="abs price" style="top:1464px">38</span>
  <p class="abs detail" style="top:1517px">2lb choice of shrimp / clams / mussel / crawfish</p>
  <span class="abs code" style="top:1569px">P2</span><span class="abs item" style="top:1569px">Snow Crab Plate</span><span class="abs price" style="top:1569px">58</span>
  <p class="abs detail" style="top:1622px">1lb snow crab &amp; 1lb choice of shrimp / clams / mussel / crawfish</p>

  <div class="divider" style="top:1670px"><svg class="squares" viewBox="0 0 30 30"><rect width="13" height="13" fill="#e0252b"/><rect x="17" width="13" height="13" fill="#e0252b"/><rect y="17" width="13" height="13" fill="#e0252b"/><rect x="17" y="17" width="13" height="13" fill="#e0252b"/></svg><div class="rule" style="width:463px"></div></div>

  <h2 class="abs section-title" style="left:243px;top:1788px">Family Meals</h2>
  <span class="abs code" style="top:1886px">M1</span><span class="abs item" style="top:1886px">Seafood Combo 3lb <small>(1 flavor)</small></span><span class="abs price" style="top:1886px">60</span>
  <p class="abs detail" style="top:1927px">choice of shrimp / clams / mussel / crawfish, ½ lb sausage,</p>
  <p class="abs detail" style="top:1962px">2 corns, 2 potato, 2 eggs, (2 cups) fountain soda</p>
  <p class="abs detail" style="top:1997px">(substitute 1lb for snow crab + 20)</p>
  <span class="abs code" style="top:2072px">M2</span><span class="abs item" style="top:2072px">Snow Crab Deluxe 4lb <small>(1 flavor)</small></span><span class="abs price" style="top:2072px">130</span>
  <p class="abs detail" style="top:2113px">six clusters of snow crab (3lb), 1lb choice of shrimp /</p>
  <p class="abs detail" style="top:2148px">clams / mussel / crawfish, 1lb sausage, 4 corns, 4 potato,</p>
  <p class="abs detail" style="top:2183px">4 eggs, (2 cups) fountain soda</p>

  <div class="divider" style="top:2231px"><svg class="squares" viewBox="0 0 30 30"><rect width="13" height="13" fill="#e0252b"/><rect x="17" width="13" height="13" fill="#e0252b"/><rect y="17" width="13" height="13" fill="#e0252b"/><rect x="17" y="17" width="13" height="13" fill="#e0252b"/></svg><div class="rule" style="width:651px"></div></div>

  <h2 class="abs section-title" style="left:0;width:724px;text-align:center;top:2348px">Flavor?</h2>
  <h2 class="abs section-title" style="left:538px;width:720px;text-align:center;top:2348px">Spice?</h2>
  <div class="col-rule"></div>
  <p class="abs choice" style="left:0;width:724px;top:2443px">Cajun (original)</p>
  <p class="abs choice" style="left:0;width:724px;top:2501px">Lemon Pepper</p>
  <p class="abs choice" style="left:0;width:724px;top:2559px">Garlic Butter</p>
  <p class="abs choice" style="left:0;width:724px;top:2617px">Bayou Bomb</p>
  <p class="abs choice" style="left:538px;width:720px;top:2443px">Non-Spicy</p>
  <p class="abs choice" style="left:538px;width:720px;top:2501px"><svg class="chili" width="28" height="40" viewBox="0 0 28 40"><path d="M22 2 C26 12 16 30 4 38 C10 26 14 14 22 2Z" fill="#4caf3c"/></svg>Mild</p>
  <p class="abs choice" style="left:538px;width:720px;top:2559px"><svg class="chili" width="50" height="40" viewBox="0 0 50 40"><path d="M22 2 C26 12 16 30 4 38 C10 26 14 14 22 2Z" fill="#4caf3c"/><path d="M44 2 C48 12 38 30 26 38 C32 26 36 14 44 2Z" fill="#4caf3c"/></svg>Medium</p>
  <p class="abs choice" style="left:538px;width:720px;top:2617px"><svg class="chili" width="72" height="40" viewBox="0 0 72 40"><path d="M22 2 C26 12 16 30 4 38 C10 26 14 14 22 2Z" fill="#4caf3c"/><path d="M44 2 C48 12 38 30 26 38 C32 26 36 14 44 2Z" fill="#4caf3c"/><path d="M66 2 C70 12 60 30 48 38 C54 26 58 14 66 2Z" fill="#4caf3c"/></svg>Hot</p>

  <div class="divider" style="top:2677px"><svg class="squares" viewBox="0 0 30 30"><rect width="13" height="13" fill="#e0252b"/><rect x="17" width="13" height="13" fill="#e0252b"/><rect y="17" width="13" height="13" fill="#e0252b"/><rect x="17" y="17" width="13" height="13" fill="#e0252b"/></svg><div class="rule" style="width:861px"></div></div>

  <h2 class="abs section-title" style="left:0;width:1200px;text-align:center;top:2772px">Drinks</h2>
  <p class="abs drink" style="top:2870px">20oz Fountain (Free Refill) 3</p>
  <p class="abs drink-sub" style="top:2912px">cola / diet cola / zero cola / lemon-lime</p>

  <p class="abs footer-title" style="top:3019px">Review us on Ratewise!</p>
  <p class="abs footer-address" style="top:3061px">4820 Harbor Ln Marin Flats, CA 90210</p>
  <div class="abs brand" style="left:126px;top:3034px"><span class="dot"></span>Reddie's Boil Shack</div>
  <div class="abs brand" style="left:968px;top:3034px"><span class="dot"></span>Reddie's Boil Shack</div>
</main>
</body>
</html>
```